Service business needs Business Card Design

Looking to create a new business card design that is both professional and unique the can highlight the many services we offer throughout the seasons. Our tagline is "The Steadfast Touch"
Licensed & Insured: PA392617 has to be small and on the back side of the card.
On the Front:
FirstName LastName
Title
We offer the following services:
Deck Repair and Maintenance
Deck Cleaning and Staining/Painting
Power Washing/House Washing
Landscape Lighting Installation
Christmas Lighting Installation

```html
<!DOCTYPE html>
<html lang="en">
<head>
<meta charset="UTF-8">
<title>Clearway Services – Business Card</title>
<link href="https://fonts.googleapis.com/css2?family=Montserrat:ital,wght@0,400;0,500;0,700;1,400&display=swap" rel="stylesheet">
<style>
  :root {
    --navy: #0b2f5f;
    --sky: #4ac4ef;
    --deep: #032d62;
    --paper: #ffffff;
    --mist: #f6f6f6;
    --edge: #2a2a2a;
  }
  * { margin: 0; padding: 0; box-sizing: border-box; }
  html, body {
    width: 1200px; height: 980px; overflow: hidden;
    background: var(--paper);
    font-family: "Montserrat", Arial, sans-serif;
  }
  .canvas { position: relative; width: 1200px; height: 980px; }

  .card {
    position: absolute; left: 330px; width: 540px; height: 330px;
    border: 1px solid var(--edge); overflow: hidden; background: var(--paper);
  }
  .card--front { top: 123px; }
  .card--back { top: 527px; }

  /* Front */
  .brand-panel {
    position: absolute; left: 11px; top: 10px; width: 242px; height: 309px;
    background: linear-gradient(to bottom, var(--sky) 0%, #2f8fc2 40%, var(--deep) 100%);
    color: var(--paper); text-align: center;
  }
  .brand-panel .wordmark {
    position: absolute; left: 0; right: 0; top: 128px;
    font-weight: 500; font-size: 19px; letter-spacing: 3px; line-height: 1.3;
    text-transform: uppercase;
  }
  .brand-panel .divider {
    position: absolute; left: 51px; width: 141px; top: 188px;
    border-top: 1.5px solid var(--paper);
  }
  .brand-panel .tagline {
    position: absolute; left: 0; right: 0; top: 203px;
    font-size: 13.5px; font-weight: 500; letter-spacing: 3.6px; line-height: 20px;
    text-transform: uppercase;
  }
  .ray-field {
    position: absolute; left: 266px; top: 3px; right: 0; bottom: 0;
    background: linear-gradient(135deg, var(--paper) 0%, var(--mist) 45%, var(--mist) 100%);
  }
  .person {
    position: absolute; left: 285px; top: 253px; color: var(--navy);
  }
  .person .name { font-weight: 700; font-size: 21px; }
  .person .title { font-style: italic; font-size: 20px; margin-top: 4px; }

  /* Back */
  .service-panel {
    position: absolute; left: 0; top: 0; width: 100%; height: 295px;
    background: linear-gradient(155deg, var(--sky) 12%, #2f91c3 42%, #15609a 68%, var(--deep) 100%);
    color: var(--paper);
  }
  .service-panel .wordmark {
    position: absolute; right: 30px; top: 70px;
    font-weight: 500; font-size: 14px; letter-spacing: 2px; line-height: 1.3;
    text-transform: uppercase; text-align: center;
  }
  .services { position: absolute; left: 31px; top: 123px; }
  .services h2 { font-weight: 700; font-size: 24px; margin-bottom: 4px; }
  .services ul { list-style: none; }
  .services li {
    position: relative; padding-left: 28px;
    font-size: 17px; line-height: 22px;
  }
  .services li::before {
    content: ""; position: absolute; left: 2px; top: 10px;
    width: 3px; height: 3px; border-radius: 50%; background: var(--paper);
  }
  .license {
    position: absolute; left: 0; right: 0; bottom: 0; height: 35px;
    display: flex; align-items: center; justify-content: center;
    color: var(--navy); font-weight: 700; font-size: 17px;
  }
</style>
</head>
<body>
<div class="canvas">
  <section class="card card--front">
    <div class="brand-panel">
      <div class="wordmark">Clearway<br>Services</div>
      <div class="divider"></div>
      <div class="tagline">The Steadfast<br>Touch</div>
    </div>
    <div class="ray-field" role="img" aria-label="Soft light grey sunburst ray backdrop"></div>
    <div class="person">
      <div class="name">FirstName LastName</div>
      <div class="title">Title</div>
    </div>
  </section>

  <section class="card card--back">
    <div class="service-panel">
      <div class="wordmark">Clearway<br>Services</div>
      <div class="services">
        <h2>Our Services</h2>
        <ul>
          <li>Deck Repair and Maintenance</li>
          <li>Deck Cleaning and Staining/Painting</li>
          <li>Power Washing/House Washing</li>
          <li>Landscape Lighting Installation</li>
          <li>Christmas Lighting Installation</li>
        </ul>
      </div>
    </div>
    <div class="license">LICENSED &amp; INSURED: PA392617</div>
  </section>
</div>
</body>
</html>
```